Banner Design Project

We are an Australian online lighting store based in Sydney.
Our website is "www.trelvamart.com.au"
We need someone you can create a 2 banners for our homepage.
We will have 3 banners rotating, the first banner will be our actual banner, the second one will be advertising Free Shipping Insurance and the third will advertising the 30 Day money back guaranty.
Don't be afraid to use words like Risk Free, 30 Day Money back Guaranty! etc....
The banner size:
599 x 186 px
The format should be given in .psd and .jpg
We need something slick and attractive that looks very promotional.
The banner should have the same look and feel as the website.
We are looking for someone long term, so if the job goes well, we might ask the person to design regularly for us in the future.

```html
<!DOCTYPE html>
<html lang="en">
<head>
<meta charset="utf-8">
<title>Trelvamart – Lighting Store</title>
<link rel="stylesheet" href="https://fonts.googleapis.com/css2?family=PT+Sans:wght@400;700&family=Open+Sans:wght@300;400;600&display=swap">
<style>
  :root {
    --orange: #f7891f;
    --orange-dark: #e2700c;
    --orange-badge: #fbb01a;
    --nav-blue: #2b5c8a;
    --nav-blue-dark: #23507a;
    --text-dark: #333333;
    --text-mid: #555555;
    --line: #d6d6d6;
    --panel-grey: #ececec;
    --why-grey: #e9e9e9;
    --header-bg: #f4f4f4;
    --white: #ffffff;
  }
  * { margin: 0; padding: 0; box-sizing: border-box; }
  html, body { width: 1200px; height: 519px; overflow: hidden; background: var(--white); }
  body { position: relative; font-family: "Open Sans", Arial, sans-serif; color: var(--text-dark); }

  .site-header { position: absolute; left: 0; top: 0; width: 1200px; height: 124px;
    background: linear-gradient(#ffffff, var(--header-bg)); }
  .brand { position: absolute; left: 30px; top: 40px; display: flex; align-items: center; gap: 12px; }
  .brand-dot { width: 34px; height: 34px; border-radius: 50%; background: var(--orange); }
  .brand-name { font-family: "PT Sans", sans-serif; font-weight: 700; font-size: 50px; color: var(--orange); line-height: 1; }

  .search { position: absolute; left: 410px; top: 53px; display: flex; height: 41px; }
  .search-input { width: 390px; height: 41px; border: 3px solid #d9d9d9; border-right: none; background: var(--white);
    font-size: 16px; color: #8a8a8a; padding: 8px 14px; }
  .search-button { width: 99px; height: 41px; background: var(--orange); color: var(--white);
    font-family: "PT Sans", sans-serif; font-weight: 700; font-size: 18px; display: flex; align-items: center; justify-content: center; letter-spacing: .3px; }

  .advice { position: absolute; left: 950px; width: 220px; top: 22px; text-align: center; color: var(--text-mid); }
  .advice-title { font-size: 18px; }
  .advice-phone { font-size: 27px; font-weight: 300; margin-top: 2px; color: #444; }
  .advice-hours { font-size: 16px; margin-top: 2px; }

  .main-nav { position: absolute; left: 17px; top: 124px; width: 1183px; height: 37px;
    background: linear-gradient(var(--nav-blue), var(--nav-blue-dark)); border-bottom: 2px solid #1c4266; }
  .main-nav span { position: absolute; top: 9px; color: var(--white); font-size: 15px; }

  .category-menu { position: absolute; left: 17px; top: 161px; width: 230px; height: 358px; }
  .category-title { position: absolute; left: 24px; font-family: "PT Sans", sans-serif; font-weight: 700; font-size: 17px; color: var(--text-dark); }
  .category-rule { position: absolute; left: 0; width: 230px; height: 1px; background: var(--line); }
  .category-item { position: absolute; left: 23px; font-size: 13px; color: var(--text-dark); }

  .hero { position: absolute; left: 249px; top: 161px; width: 720px; height: 223px;
    background: linear-gradient(100deg, #e8ecef 0%, #c9d2da 25%, #6d8aa8 45%, #dfe3e6 60%, #cfcac4 75%, #f3f3f3 100%); }
  .hero-offer { position: absolute; left: 729px; top: 184px; width: 212px; height: 212px; border-radius: 50%;
    background: var(--orange-badge); display: flex; flex-direction: column; align-items: center; justify-content: center;
    font-family: "PT Sans", sans-serif; font-weight: 700; font-size: 29px; line-height: 34px; color: var(--white); text-align: center; }

  .newsletter { position: absolute; left: 253px; top: 395px; width: 704px; height: 82px; background: var(--panel-grey); }
  .newsletter-icon { position: absolute; left: 12px; top: 2px; }
  .newsletter-title { position: absolute; left: 99px; top: 17px; font-family: "PT Sans", sans-serif; font-weight: 700; font-size: 17px; color: var(--text-dark); }
  .newsletter-title b { color: var(--nav-blue); }
  .newsletter-label { position: absolute; left: 125px; top: 47px; font-family: "PT Sans", sans-serif; font-size: 16px; }
  .newsletter-input { position: absolute; left: 216px; top: 46px; width: 310px; height: 26px; background: var(--white); border: 1px solid #c5c5c5; }
  .newsletter-button { position: absolute; left: 530px; top: 47px; width: 85px; height: 24px; background: var(--orange);
    color: var(--white); font-family: "PT Sans", sans-serif; font-weight: 700; font-size: 16px; text-align: center; line-height: 24px; }

  .content-strip { position: absolute; left: 253px; top: 505px; width: 704px; height: 14px; background: var(--panel-grey); }

  .cart { position: absolute; left: 972px; top: 161px; width: 228px; height: 237px; }
  .cart-icon { position: absolute; left: 25px; top: 32px; width: 48px; height: 48px; border-radius: 8px;
    background: linear-gradient(#fafafa, #dcdcdc); border: 1px solid #c8c8c8; }
  .cart-icon svg { position: absolute; left: 9px; top: 10px; }
  .cart-title { position: absolute; left: 87px; top: 24px; font-family: "PT Sans", sans-serif; font-weight: 700; font-size: 24px; line-height: 29px; color: var(--text-dark); }
  .cart-line { position: absolute; left: 23px; font-family: "PT Sans", sans-serif; font-size: 17px; color: var(--text-dark); }
  .cart-line b { font-weight: 700; }
  .checkout { position: absolute; left: 23px; top: 175px; width: 181px; height: 38px; background: linear-gradient(var(--orange), var(--orange-dark));
    color: var(--white); font-family: "PT Sans", sans-serif; font-weight: 700; font-size: 19px; text-align: center; line-height: 38px; }

  .why { position: absolute; left: 972px; top: 398px; width: 228px; height: 121px; }
  .why-head { height: 67px; background: var(--why-grey); text-align: center; font-family: "PT Sans", sans-serif; font-weight: 700;
    font-size: 22px; line-height: 67px; color: var(--nav-blue); }
  .why-point { position: absolute; left: 25px; top: 78px; display: flex; gap: 10px; }
  .why-point p { font-size: 14px; line-height: 17px; color: var(--text-dark); margin-top: 6px; }
</style>
</head>
<body>
  <header class="site-header">
    <div class="brand"><span class="brand-dot"></span><span class="brand-name">Trelvamart</span></div>
    <div class="search">
      <div class="search-input">Type in Keyword, Brand or item#</div>
      <div class="search-button">SEARCH</div>
    </div>
    <div class="advice">
      <div class="advice-title">Need Expert Advice?</div>
      <div class="advice-phone">1300 472 915</div>
      <div class="advice-hours">Mon-Fri 9am - 5pm</div>
    </div>
  </header>

  <nav class="main-nav">
    <span style="left:29px">Home</span>
    <span style="left:142px">About Us</span>
    <span style="left:280px">Testimonials</span>
    <span style="left:433px">Customer Care</span>
    <span style="left:605px">Contact Us</span>
    <span style="left:899px">My Shortlist</span>
    <span style="left:1010px">My Account</span>
    <span style="left:1124px">Login</span>
  </nav>

  <aside class="category-menu">
    <div class="category-title" style="top:8px">Indoor Lighting</div>
    <div class="category-rule" style="top:36px"></div>
    <div class="category-item" style="top:49px">Ceiling Fans</div>
    <div class="category-item" style="top:77px">Ceiling Lights</div>
    <div class="category-item" style="top:105px">Wall Lights</div>
    <div class="category-item" style="top:133px">Table and Floor Lamps</div>
    <div class="category-item" style="top:161px">Kids Lighting</div>
    <div class="category-item" style="top:189px">LED / Energy Savers</div>
    <div class="category-rule" style="top:216px"></div>
    <div class="category-title" style="top:225px">Outdoor Lighting</div>
    <div class="category-rule" style="top:254px"></div>
    <div class="category-item" style="top:266px">Garden Lights</div>
    <div class="category-item" style="top:294px">LED/Energy Savers</div>
    <div class="category-item" style="top:322px">In Ground Lights</div>
    <div class="category-item" style="top:350px">Bollards/Post Lights</div>
  </aside>

  <div class="hero" role="img" aria-label="Photo of three smiling delivery and office staff in front of a warehouse with parcels"></div>
  <div class="hero-offer"><span>FREE</span><span>SHIPPING</span><span>INSURANCE</span></div>

  <section class="newsletter">
    <svg class="newsletter-icon" width="84" height="84" viewBox="0 0 84 84" aria-hidden="true">
      <g transform="rotate(-14 42 42)">
        <rect x="8" y="20" width="68" height="46" fill="#f4f4f4" stroke="#9a9a9a" stroke-width="2"/>
        <path d="M8 20 L42 48 L76 20" fill="none" stroke="#9a9a9a" stroke-width="2"/>
      </g>
    </svg>
    <div class="newsletter-title"><b>Join the Trelvamart Newsletter</b> - Sales, special offers and more</div>
    <div class="newsletter-label">Enter Email:</div>
    <div class="newsletter-input"></div>
    <div class="newsletter-button">Sign Up</div>
  </section>
  <div class="content-strip"></div>

  <aside class="cart">
    <div class="cart-icon">
      <svg width="30" height="28" viewBox="0 0 30 28" aria-hidden="true">
        <path d="M2 4 H7 L11 18 H24 L27 8 H9" fill="none" stroke="#333" stroke-width="2.5" stroke-linejoin="round"/>
        <circle cx="12" cy="23" r="2.5" fill="#333"/><circle cx="23" cy="23" r="2.5" fill="#333"/>
      </svg>
    </div>
    <div class="cart-title">Shopping<br>Cart</div>
    <div class="cart-line" style="top:108px"><b>Items:</b> 0</div>
    <div class="cart-line" style="top:129px"><b>Total:</b> $0.00</div>
    <div class="checkout">CHECKOUT</div>
  </aside>

  <aside class="why">
    <div class="why-head">Why Trelvamart?</div>
    <div class="why-point">
      <svg width="20" height="20" viewBox="0 0 20 20" aria-hidden="true"><path d="M2 11 L7 16 L18 3" fill="none" stroke="#9a9a9a" stroke-width="2.5"/></svg>
      <p>30 Day Money Back<br>Guarantee</p>
    </div>
  </aside>
</body>
</html>
```